Redesigning a responsive newsletter template

Recoding/redesigning a responsive newsletter template called PostLoom.

http://layoutbazaar.example/item/postloom-responsive-email-template/5283906

I have already assembled the newsletter template through an online editor, however I need a few modifications, which the instructions will outline. This should be pretty basic and easy.

Colors
00a990

Requirements
Must have
• Template must remain responsive on all devices.
• Designer must have SendKite account. It's very easy to get a free account. I will send you the template through SendKite.
• Send your email address to darylbrewick42@quillpost.example. I will send you the template.
• After modifying it (use the instructions), send it back to me through SendKite "Templates" page - right side drop down "Edit" menu "Share" button.
Nice to have
• Follow instructions and provide design ideas.

```html
<!DOCTYPE html>
<html lang="en">
<head>
<meta charset="utf-8">
<title>PostLoom Newsletter</title>
<link href="https://fonts.googleapis.com/css2?family=Roboto:wght@300;400&display=swap" rel="stylesheet">
<style>
  :root {
    --teal: #00a990;
    --teal-link: #2a9fb5;
    --page: #eae8e8;
    --card: #ffffff;
    --title: #555a60;
    --body: #9a9a9a;
    --rule: #e3e3e3;
    --red: #d9534f;
  }
  * { box-sizing: border-box; margin: 0; padding: 0; }
  html, body { width: 878px; height: 1200px; overflow: hidden; background: #fff; }
  body { font-family: "Roboto", Arial, sans-serif; font-weight: 300; position: relative; }
  .page { position: absolute; left: 15px; top: 0; width: 848px; height: 1200px; background: var(--page); }
  .column { position: absolute; left: 106px; width: 636px; }
  .teal-bar { position: absolute; left: 106px; width: 636px; height: 11px; background: var(--teal);
    box-shadow: 0 6px 8px -4px rgba(0,0,0,.18); }
  .support-card { top: 48px; height: 198px; background: var(--card); }
  .support-card h2 { position: absolute; left: 20px; top: 22px; font-size: 19px; font-weight: 300; color: var(--title); }
  .support-card p { position: absolute; left: 20px; top: 63px; width: 270px; font-size: 13px; line-height: 23px; color: var(--body); }
  .photo { position: absolute; }
  .support-photo { left: 329px; top: 21px; width: 286px; height: 155px;
    background: linear-gradient(180deg, #e8eef4 0%, #dfe8f0 55%, #b9cee0 62%, #cdd9e3 100%); }
  .feature { top: 289px; height: 559px; background: var(--card); }
  .hero-photo { left: 0; top: 0; width: 636px; height: 424px;
    background: linear-gradient(180deg, #eef2f4 0%, #dfe4e6 55%, #c9c4bc 80%, #8a6a4f 100%); }
  .feature-text { position: absolute; left: 40px; top: 445px; width: 556px; text-align: center;
    font-size: 13px; line-height: 23px; color: var(--body); }
  .announce { top: 848px; height: 172px; background: var(--card); border-top: 1px solid var(--rule); }
  .announce h3 { position: absolute; left: 42px; top: 21px; font-size: 23px; font-weight: 300; color: var(--teal-link); }
  .announce .meta { position: absolute; left: 42px; top: 53px; font-size: 13px; color: var(--body); }
  .announce p { position: absolute; left: 42px; top: 89px; width: 548px; font-size: 13px; line-height: 23px; color: var(--body); }
  .social { top: 1020px; height: 54px; background: var(--card); border-top: 1px solid var(--rule);
    display: flex; justify-content: center; align-items: center; gap: 12px; }
  .social span { font-size: 11px; font-weight: 400; color: var(--teal-link); }
  .prefs { position: absolute; left: 0; width: 848px; top: 1100px; text-align: center; font-size: 13px; color: var(--teal-link); font-weight: 400; }
  .prefs .sep { color: var(--red); margin: 0 3px 0 6px; }
  .footer { position: absolute; left: 0; top: 1143px; width: 848px; height: 47px; background: var(--teal);
    color: #fff; font-size: 13px; font-weight: 400; text-align: center; line-height: 47px; }
</style>
</head>
<body>
  <div class="page">
    <div class="teal-bar" style="top:4px"></div>

    <section class="column support-card">
      <h2>Support MailHarbor</h2>
      <p>Lorem ipsum dolor sit amet, consetetur sadipscing elitr, sed diam nonumy eirmod .</p>
      <div class="photo support-photo" role="img" aria-label="Woman meditating cross-legged by the sea"></div>
    </section>
    <div class="teal-bar" style="top:246px"></div>

    <section class="column feature">
      <div class="photo hero-photo" role="img" aria-label="Three women stretching on yoga mats in a bright studio"></div>
      <p class="feature-text">Lorem ipsum dolor sit amet, consetetur sadipscing elitr, sed diam nonumy eirmod tempam et justo duo dolores et ea rebum. Lorem ipsum dolor sit amet, consetetur sadipscing elitr, sed diam nonumy eirmod tempam et justo duo dolores et ea rebum.</p>
    </section>

    <section class="column announce">
      <h3>Announce even</h3>
      <div class="meta">by anynone 12/02/2014</div>
      <p>Lorem ipsum dolor sit amet, consetetur sadipscing elitr, sed diam nonumy eirmod tempam et justo duo dolores et ea rebum. Lorem ipsum</p>
    </section>

    <nav class="column social" aria-label="Social links">
      <span>Zorvik</span><span>Quello</span><span>Marrowin</span><span>Tevlane</span>
      <span>Oskaray</span><span>Brindell</span><span>Yarnoth</span><span>Kestrum</span>
    </nav>

    <div class="prefs">unsubscribe <span class="sep">|</span>update preference <span class="sep">|</span>visit website</div>

    <footer class="footer">Your company here , all rights reserved 2013 ©</footer>
  </div>
</body>
</html>
```